We need a tri-fold brochure design.

We need a tri-fold brochure design to highlight our Lanternwood Seed Program. The brochure we have now is functional, but we would like a design that is eye catching. We have a sample brochure that we have attached with the wording we would like to include for the brochure. We would like something that will catch a potential donor’s eye.
Updates

The tri-fold brochure should be in the same order as the sample brochure that was attached. The descriptions align with the photos. We would like to use the same cover shot that is on the sample photo. Thank you. Added Saturday, March 28, 2015

Target Market(s)

This brochure will be given out to potential donors.

Colors
3176b5

Requirements
Must have
• It must be eye catching.
Nice to have
• We would like to have something that will be engaging and make people want to give to our agency.
Should not have
• We don't want the kiddie text.

```html
<!DOCTYPE html>
<html lang="en">
<head>
<meta charset="utf-8">
<title>Lanternwood Seed Program – Grant Highlights</title>
<link href="https://fonts.googleapis.com/css2?family=PT+Sans+Narrow:wght@400;700&display=swap" rel="stylesheet">
<style>
  :root {
    --brand-blue: #2c5fa9;
    --page-bg: #ffffff;
    --frame-light: #e4e4e4;
    --frame-mid: #b9b9b9;
    --frame-dark: #8e8e8e;
    --card-top: #444444;
    --card-bottom: #1f1f1f;
    --card-text: #ececec;
  }
  * { box-sizing: border-box; margin: 0; padding: 0; }
  html, body { width: 1200px; height: 930px; overflow: hidden; background: var(--page-bg); }
  .spread {
    position: relative;
    width: 1200px;
    height: 930px;
    font-family: "PT Sans Narrow", "Arial Narrow", sans-serif;
  }
  .blue-band {
    position: absolute;
    left: 0; right: 0;
    top: 138px; height: 664px;
    background: var(--brand-blue);
  }
  .photo-frame {
    position: absolute;
    width: 333px;
    height: 224px;
    padding: 9px;
    background: linear-gradient(160deg, var(--frame-light), var(--frame-mid) 55%, var(--frame-dark));
    box-shadow: 0 3px 8px rgba(0,0,0,.45);
  }
  .photo-frame .photo {
    width: 100%;
    height: 100%;
    box-shadow: inset 0 0 0 1px rgba(0,0,0,.35);
  }
  .pointer {
    position: absolute;
    left: 50%;
    width: 40px; height: 20px;
    margin-left: -20px;
  }
  .photo-frame.top .pointer { bottom: -19px; }
  .photo-frame.bottom .pointer { top: -19px; }
  .story {
    position: absolute;
    width: 333px;
    padding: 18px 12px 12px;
    background: linear-gradient(180deg, var(--card-top), var(--card-bottom));
    color: var(--card-text);
    font-size: 15.5px;
    line-height: 19.5px;
    box-shadow: 0 3px 8px rgba(0,0,0,.4);
  }
  .col-1 { left: 33px; }
  .col-2 { left: 430px; }
  .col-3 { left: 827px; }
  .row-top.photo-frame { top: 21px; }
  .row-top.story { top: 262px; height: 218px; }
  .row-bottom.story { top: 509px; height: 136px; }
  .row-bottom.photo-frame { top: 682px; }
</style>
</head>
<body>
<main class="spread">
  <div class="blue-band"></div>

  <figure class="photo-frame top row-top col-1">
    <div class="photo" role="img" aria-label="Group of junior high science students in a lab holding grant signs" style="background:linear-gradient(160deg,#8a7a66,#5b4f44 60%,#3c3630)"></div>
    <svg class="pointer" viewBox="0 0 40 20"><polygon points="0,0 40,0 20,20" fill="#a3a3a3"/></svg>
  </figure>
  <p class="story row-top col-1">Marisol Vantree, along with Dean Holloway, at Brookhaven Junior High received two grants totaling $2,653. These grants enabled both teachers to give their junior high science students a better understanding of chemistry and physics as well as a deeper understanding of the earth through hands-on activities and equipment.</p>

  <figure class="photo-frame top row-top col-2">
    <div class="photo" role="img" aria-label="Elementary class gathered in a decorated classroom holding grant signs" style="background:linear-gradient(160deg,#6f6a6e,#4a4a55 60%,#3a3438)"></div>
    <svg class="pointer" viewBox="0 0 40 20"><polygon points="0,0 40,0 20,20" fill="#a3a3a3"/></svg>
  </figure>
  <p class="story row-top col-2">Nora Castell, Willow Bend Elementary, was awarded four grants totaling $2,885. Three of these grants are designed to improve reading levels, interest in reading, and passion for reading in elementary students by increasing the availability of Pathfinder Reader books, Starling Award books, and audio books. The fourth grant provides supplies and materials to reintroduce Fine Arts at the elementary level through art and drama.</p>

  <figure class="photo-frame top row-top col-3">
    <div class="photo" role="img" aria-label="Elementary students and staff in a bright classroom holding grant signs" style="background:linear-gradient(160deg,#a9a29a,#6c6470 60%,#4a4452)"></div>
    <svg class="pointer" viewBox="0 0 40 20"><polygon points="0,0 40,0 20,20" fill="#a3a3a3"/></svg>
  </figure>
  <p class="story row-top col-3">Tessa Marlow, Ashgrove Elementary, was awarded three grants totaling $981. Two of these grants provide books to help increase reading proficiency, enthusiasm about reading, and provide essential knowledge of scientific concepts as well as reinforce the importance of STEM (science, technology, engineering, and math) in a creative way. The third grant provides supplies and materials for the newly-formed elementary art club.</p>

  <p class="story row-bottom col-1">Elaine Porter, Fernridge Elementary, received one grant for $2,348. Books purchased through this grant will help her first grade students to become successful readers by challenging them to read more books and increase their reading level at this important stage in their education.</p>
  <figure class="photo-frame bottom row-bottom col-1">
    <svg class="pointer" viewBox="0 0 40 20"><polygon points="0,20 40,20 20,0" fill="#d6d6d6"/></svg>
    <div class="photo" role="img" aria-label="First grade class seated on the floor of a classroom with grant signs" style="background:linear-gradient(160deg,#b3b6a4,#7d7f70 60%,#545548)"></div>
  </figure>

  <p class="story row-bottom col-2">Rafael Ortega, Harborview Elementary, received two grants totaling $715. These grants involve giving elementary students a better understanding of the sun and its properties and learning weather forecasting abilities.</p>
  <figure class="photo-frame bottom row-bottom col-2">
    <svg class="pointer" viewBox="0 0 40 20"><polygon points="0,20 40,20 20,0" fill="#d6d6d6"/></svg>
    <div class="photo" role="img" aria-label="Elementary students crowded together holding grant signs and checks" style="background:linear-gradient(160deg,#8f8a80,#5e5a5a 60%,#3e3c44)"></div>
  </figure>

  <p class="story row-bottom col-3">Danielle Ruiz-Carver, Fernridge Junior High, received a $1,000 grant to help implement technology into the musical classroom. This grant includes a tablet and a number of applications to assist junior high students in creating their own music and tuning their instruments.</p>
  <figure class="photo-frame bottom row-bottom col-3">
    <svg class="pointer" viewBox="0 0 40 20"><polygon points="0,20 40,20 20,0" fill="#d6d6d6"/></svg>
    <div class="photo" role="img" aria-label="Junior high orchestra students with violins in a hallway of lockers" style="background:linear-gradient(160deg,#8a4a44,#5a3a3a 60%,#3b2c30)"></div>
  </figure>
</main>
</body>
</html>
```